Asia based real estate financing firm needs and AWESOME design for a biz card -Harbor Lending Circle

Looking for a stylish, & corporate-looking business card for a real estate financing brokerage firm in Asia, offering global mortgage loans. I uploaded our current logos. We would like to add a splash of color (perhaps the house icon) or any other suggestions are open. For the winning designer, we have a lot of work! Thanks and best of luck!

Target Market(s)

Real estate investors globally. We want to look more like a BANK and NOT a real estate company. Please don't play up on a "house" design.

Industry/Entity Type

Banking

Contact Information for Business Card

Harbor Lending Circle
Peter Wilks
Co-Founder | Partner

14 Cassia Lane, Suite 310
Singapore 047219
www.hlc-example.asia
peterwilks@hlc-example.asia
+65 555-0142
WeChat: peterwilks

Colors

Designer to choose colors to be used in the design.

Requirements
Must have
• Must have the standard business requirements for a card; name, address, email, etc
• Can be horizontal or vertical.
Nice to have
• It would be great to see some sort of variation to the logo with a pop of color. Red is good as we're in Asia, however, other options work as well.
• Our tag line is - Borderless mortgages. It doesn't have to be on the card but might be nice.
• I'd like to start seeing our tagline within the cards as well. - Borderless mortgages.
• Also, please add our location. The location for this card is Singapore so perhaps it can be highlighted or emphasised in some way.
• Singapore | Hong Kong | Shanghai | Manila
• As we will soon open an office in Shanghai, having an option for both languages would be great.
Should not have
• I'm exceited and open to your creativity ... knock it out of the park!

```html
<!DOCTYPE html>
<html lang="en">
<head>
<meta charset="utf-8">
<title>Harbor Lending Circle – Business Card</title>
<link rel="stylesheet" href="https://fonts.googleapis.com/css2?family=Tinos&family=PT+Sans+Narrow:wght@700&family=Source+Sans+3:wght@400&display=swap">
<style>
  :root {
    --stage: #676767;
    --paper: #ffffff;
    --ink: #171c1c;
    --amber: #fea60b;
    --flame: #fd5d0a;
    --mist: #e8ebeb;
    --serif: "Tinos", serif;
    --narrow: "PT Sans Narrow", sans-serif;
    --sans: "Source Sans 3", sans-serif;
  }
  html, body {
    margin: 0;
    width: 1200px;
    height: 1200px;
    overflow: hidden;
    background: var(--stage);
  }
  .card {
    position: absolute;
    top: 209.6px;
    width: 468px;
    height: 780.8px;
    display: block;
  }
  .card--front { left: 101.6px; }
  .card--back { left: 629.6px; }
  .brand-name { font-family: var(--serif); fill: var(--ink); text-anchor: middle; }
  .front-url { font-family: var(--sans); font-size: 31px; fill: var(--ink); text-anchor: middle; }
  .holder-name { font-family: var(--narrow); font-size: 44px; fill: var(--ink); text-anchor: middle; }
  .holder-role { font-family: var(--narrow); font-size: 35px; fill: var(--ink); text-anchor: middle; }
  .contact-text { font-family: var(--sans); font-size: 31px; fill: var(--paper); }
  .icon-tile { fill: var(--paper); }
  .icon-mark { fill: var(--flame); }
  .icon-line { fill: none; stroke: var(--paper); stroke-width: 2; }
</style>
</head>
<body>

<!-- Front of card -->
<svg class="card card--front" viewBox="0 0 585 976" aria-label="Card front">
  <rect width="585" height="976" fill="var(--paper)"/>
  <g class="edge-top">
    <rect width="585" height="58" fill="var(--ink)"/>
    <polygon points="88,0 503,0 446,99 145,99" fill="var(--amber)"/>
    <polygon points="0,0 38,0 95,99 58,99" fill="var(--flame)"/>
    <polygon points="585,0 547,0 490,99 527,99" fill="var(--flame)"/>
  </g>
  <g class="brand-lockup">
    <rect x="281" y="372" width="22" height="22" fill="var(--ink)"/>
    <text class="brand-name" x="292.5" y="470" font-size="64" letter-spacing="6">HARBOR</text>
    <text class="brand-name" x="292.5" y="540" font-size="64" letter-spacing="6">LENDING</text>
    <text class="brand-name" x="292.5" y="610" font-size="64" letter-spacing="6">CIRCLE</text>
  </g>
  <g class="edge-bottom">
    <rect y="918" width="585" height="58" fill="var(--ink)"/>
    <polygon points="88,976 503,976 446,877 145,877" fill="var(--amber)"/>
    <polygon points="0,976 38,976 95,877 58,877" fill="var(--flame)"/>
    <polygon points="585,976 547,976 490,877 527,877" fill="var(--flame)"/>
    <text class="front-url" x="292.5" y="940">www.hlc-example.asia</text>
  </g>
</svg>

<!-- Back of card -->
<svg class="card card--back" viewBox="0 0 585 976" aria-label="Card back">
  <rect width="585" height="976" fill="var(--paper)"/>
  <rect y="438" width="585" height="48" fill="var(--mist)"/>
  <rect y="486" width="585" height="490" fill="var(--ink)"/>

  <g class="edge-top">
    <rect width="585" height="53" fill="var(--ink)"/>
    <polygon points="97,0 488,0 447,73 138,73" fill="var(--amber)"/>
    <polygon points="35,0 65,0 103,73 73,73" fill="var(--flame)"/>
    <polygon points="550,0 520,0 482,73 512,73" fill="var(--flame)"/>
  </g>

  <g class="brand-lockup">
    <rect x="284" y="170" width="16" height="16" fill="var(--ink)"/>
    <text class="brand-name" x="292.5" y="240" font-size="46" letter-spacing="4">HARBOR</text>
    <text class="brand-name" x="292.5" y="292" font-size="46" letter-spacing="4">LENDING</text>
    <text class="brand-name" x="292.5" y="344" font-size="46" letter-spacing="4">CIRCLE</text>
  </g>

  <g class="name-ribbon">
    <polygon points="78,438 98,412 130,463 98,514 78,488" fill="var(--flame)"/>
    <polygon points="507,438 487,412 455,463 487,514 507,488" fill="var(--flame)"/>
    <polygon points="101,398 484,398 441,463 144,463" fill="var(--amber)"/>
    <polygon points="144,463 441,463 484,528 101,528" fill="var(--flame)"/>
    <polyline points="101,398 144,463 101,528" fill="none" stroke="var(--ink)" stroke-width="14"/>
    <polyline points="484,398 441,463 484,528" fill="none" stroke="var(--ink)" stroke-width="14"/>
    <text class="holder-name" x="292.5" y="447">PETER WILKS</text>
    <text class="holder-role" x="292.5" y="510">Co-Founder | Partner</text>
  </g>

  <g class="contact-list">
    <g class="contact-row">
      <rect class="icon-tile" x="53" y="563" width="38" height="38"/>
      <circle class="icon-mark" cx="72" cy="582" r="14"/>
      <path d="M72 572a6 6 0 0 1 6 6c0 5-6 12-6 12s-6-7-6-12a6 6 0 0 1 6-6z" fill="var(--paper)"/>
      <circle cx="72" cy="578" r="2.2" class="icon-mark"/>
      <text class="contact-text" x="117" y="592">14 Cassia Lane, Suite 310</text>
      <text class="contact-text" x="117" y="636">Singapore-047219</text>
    </g>
    <g class="contact-row">
      <rect class="icon-tile" x="53" y="660" width="38" height="38"/>
      <circle class="icon-mark" cx="72" cy="679" r="14"/>
      <rect x="66" y="669" width="12" height="20" rx="2" class="icon-line"/>
      <text class="contact-text" x="117" y="690">+65 555-0142</text>
    </g>
    <g class="contact-row">
      <rect class="icon-tile" x="53" y="712" width="38" height="38"/>
      <circle class="icon-mark" cx="72" cy="731" r="14"/>
      <rect x="63" y="725" width="18" height="13" class="icon-line"/>
      <polyline points="63,725 72,733 81,725" class="icon-line"/>
      <text class="contact-text" x="117" y="740">peterwilks@hlc-example.asia</text>
    </g>
    <g class="contact-row">
      <rect class="icon-tile" x="53" y="765" width="38" height="38"/>
      <g fill="none" stroke="var(--flame)" stroke-width="2">
        <circle cx="72" cy="784" r="13"/>
        <ellipse cx="72" cy="784" rx="6" ry="13"/>
        <line x1="59" y1="784" x2="85" y2="784"/>
        <line x1="61" y1="777" x2="83" y2="777"/>
        <line x1="61" y1="791" x2="83" y2="791"/>
      </g>
      <text class="contact-text" x="117" y="793">www.hlc-example.asia</text>
    </g>
    <g class="contact-row">
      <rect class="icon-tile" x="53" y="818" width="38" height="38"/>
      <path d="M60 829h24v14h-14l-6 5v-5h-4z" fill="var(--flame)"/>
      <text class="contact-text" x="117" y="846">peterwilks</text>
    </g>
  </g>

  <g class="edge-bottom">
    <polygon points="138,903 447,903 488,976 97,976" fill="var(--amber)"/>
    <polygon points="35,976 65,976 103,903 73,903" fill="var(--paper)"/>
    <polygon points="550,976 520,976 482,903 512,903" fill="var(--paper)"/>
  </g>
</svg>

</body>
</html>
```